Ora- luxurious rental suites coming soon

Looking for a large size banner design. The banner will include the logo "ORA". The logo has already been designed by one of your designers (Belmiro). The banner is to be placed on the building fence and will be used as a marketing/ advertisement purpose to display what's coming soon. It needs to be clean and elegant since it's representing upscale apartements.
Requesting Belmiro to be one of the designers. Thanks.
Updates

Hi all-here is the logo link. Banner will be printed on 3 separate boards that will be attached side by side to look like one big one. We are doing it this way to be able to make future modifications on 1 board at a time. Each board will be 10'Wx8'H panel. Logo design needs to be in the middle board and other left and right side boards will have the info like "coming soon and building picture". For now, please use any building image, I will be sending the actual building image later on for an update. Please do not include full image of building, choose a section and zoom or crop portion of building image so it looks more interesting. Building will be a luxurious rental in downtown. Thanks. https://www.filecrate.net/sh/k4mwpxq7r2d9vzb/QRT8LMN2K_hx_WBZcpfkeH3Lo?dl=0x

Re: banner: Instead of "coming soon" please use "coming this fall'. Thanks

Target Market(s)

professionals

Industry/Entity Type

Residential rentals

Font styles to use
Serif

Requirements
Must have
• use wording such as: coming this fall, 1&2 bedroom suites, designer finishes, terrace views
Nice to have
• Banner will be placed on site over a black mesh backdrop. Please design in a way that will make it look like blending with mesh
Should not have
• Banner should not be too colorf. Please use white, grey or yellow... refer to logo image

```html
<!DOCTYPE html>
<html lang="en">
<head>
<meta charset="utf-8">
<title>ORA – Luxurious Rental Suites Fence Banner</title>
<link rel="stylesheet" href="https://fonts.googleapis.com/css2?family=Montserrat:wght@300;400&family=Open+Sans:wght@700&display=swap">
<style>
  :root {
    --charcoal: #231f20;
    --divider: #5a5a5a;
    --paper: #ffffff;
    --gold: #f5c400;
    --gold-soft: #fbe27a;
    --ink: #1c1c1c;
    --sky: #cfe2f3;
    --glass-light: #6e9ed0;
    --glass-deep: #1f5395;
  }
  html, body {
    margin: 0;
    padding: 0;
    width: 1200px;
    height: 321px;
    overflow: hidden;
    background: var(--paper);
  }
  .banner { display: block; width: 1200px; height: 321px; }
  .board { fill: var(--charcoal); }
  .board-gap { fill: var(--divider); }
  .tagline {
    font-family: "Open Sans", sans-serif;
    font-weight: 700;
    fill: var(--gold);
  }
  .tagline--coming { font-size: 38px; }
  .tagline--headline { font-size: 37px; letter-spacing: 0.5px; }
  .feature-list {
    font-family: "Open Sans", sans-serif;
    font-weight: 700;
    font-size: 19px;
    fill: var(--ink);
  }
  .brand-name {
    font-family: "Montserrat", sans-serif;
    font-weight: 300;
    font-size: 138px;
    letter-spacing: 4px;
    fill: var(--paper);
  }
  .brand-address {
    font-family: "Montserrat", sans-serif;
    font-weight: 400;
    font-size: 19px;
    letter-spacing: 6px;
    fill: var(--paper);
  }
</style>
</head>
<body>
<svg class="banner" viewBox="0 0 1200 321" xmlns="http://www.w3.org/2000/svg">
  <defs>
    <linearGradient id="halftone-left" x1="0" y1="1" x2="1" y2="0">
      <stop offset="0" stop-color="var(--gold)" stop-opacity="0.75"/>
      <stop offset="0.5" stop-color="var(--gold-soft)" stop-opacity="0.45"/>
      <stop offset="1" stop-color="var(--paper)" stop-opacity="0.25"/>
    </linearGradient>
    <linearGradient id="halftone-centre" x1="1" y1="1" x2="0" y2="0">
      <stop offset="0" stop-color="var(--gold)" stop-opacity="0.75"/>
      <stop offset="1" stop-color="var(--gold-soft)" stop-opacity="0.35"/>
    </linearGradient>
    <linearGradient id="glass-facade" x1="0" y1="0" x2="1" y2="1">
      <stop offset="0" stop-color="var(--sky)"/>
      <stop offset="0.4" stop-color="var(--glass-light)"/>
      <stop offset="1" stop-color="var(--glass-deep)"/>
    </linearGradient>
    <linearGradient id="halftone-sky" x1="0" y1="0" x2="1" y2="1">
      <stop offset="0" stop-color="var(--gold)" stop-opacity="0.55"/>
      <stop offset="0.6" stop-color="var(--gold-soft)" stop-opacity="0"/>
    </linearGradient>
  </defs>

  <!-- left board -->
  <rect class="board" x="0" y="0" width="394" height="315"/>
  <polygon role="img" aria-label="Yellow and white halftone dot field fading diagonally"
           fill="url(#halftone-left)" points="156,315 394,162 394,315"/>
  <text class="tagline tagline--coming" transform="translate(114,303) rotate(-35)">...coming this fall</text>

  <rect class="board-gap" x="394" y="0" width="8" height="315"/>

  <!-- centre board -->
  <rect class="board" x="402" y="0" width="395" height="315"/>
  <polygon role="img" aria-label="Yellow halftone dot band along the lower left edge"
           fill="url(#halftone-centre)" points="402,156 494,315 402,315"/>
  <polygon role="img" aria-label="Yellow halftone dot band along the upper right edge"
           fill="url(#halftone-centre)" points="720,0 797,0 797,144"/>
  <text class="brand-address" transform="translate(537,126) rotate(-34)">415 HALDEN</text>
  <text class="brand-name" transform="translate(492,303) rotate(-34)">ORA</text>

  <rect class="board-gap" x="797" y="0" width="7" height="315"/>

  <!-- right board -->
  <rect role="img" aria-label="Close-up photograph of a glass tower facade looking up at the sky"
        fill="url(#glass-facade)" x="804" y="0" width="396" height="315"/>
  <polygon role="img" aria-label="Yellow halftone dot field over the sky"
           fill="url(#halftone-sky)" points="804,0 1010,0 804,170"/>
  <text class="feature-list" transform="translate(828,134) rotate(-32)">1&amp;2 bedroom suites</text>
  <text class="feature-list" transform="translate(842,154) rotate(-32)">designer finishes</text>
  <text class="tagline tagline--headline" transform="translate(902,248) rotate(-34)">LUXURIOUS</text>
  <text class="tagline tagline--headline" transform="translate(928,287) rotate(-34)">RENTAL SUITES</text>
</svg>
</body>
</html>
```